Business Card Design

I am a Building Surveyor and run my own Building Consultat company, providing professional advice and services to builders, architects, designers, owners, etc.

Industry/Entity Type

Business

Contact Information for Business Card

Dorwen Halket BBldgSurv (Hons)
Managing Director

57 Quillon Rise, Marrick Heights WA 6148
Mobile 0438 271 594
Email Dorwen.halket@tarnwellpq.com

Requirements
Must have
• I would like the back of the business card to be one colour (a shade of either black or maroon, matching the colours of my logo). Positioned in the centre on the back of the business card is to be my logo.

The front of the card is to be white, with my contact information in either black or maroon. The ADBldgSurv after my name should be in a smaller font size than my name. I would also like a small logo somewhere on this side of the card.

```html
<!DOCTYPE html>
<html lang="en">
<head>
<meta charset="utf-8">
<title>Tarnwell Building Consultants – Business Card</title>
<link rel="stylesheet" href="https://fonts.googleapis.com/css2?family=EB+Garamond:wght@400;500&display=swap">
<style>
  :root {
    --maroon: #69271e;
    --ink: #3b3b3b;
    --mark-grey: #454545;
    --card-edge: #a3a3a3;
    --paper: #ffffff;
    --page: #ffffff;
  }
  * { box-sizing: border-box; margin: 0; padding: 0; }
  html, body {
    width: 984px; height: 1200px; overflow: hidden;
    background: var(--page);
    font-family: "EB Garamond", Garamond, serif;
  }
  .canvas { position: relative; width: 984px; height: 1200px; }

  .card {
    position: absolute; left: 46px; width: 885px; height: 536px;
  }
  .card--front { top: 38px; background: var(--paper); border: 1px solid var(--card-edge); }
  .card--back { top: 602px; background: var(--maroon); }

  /* front logo lockup */
  .brand-front { position: absolute; left: 78px; top: 50px; display: flex; align-items: center; }
  .brand-front__dot {
    width: 146px; height: 146px; border-radius: 50%; background: var(--maroon);
  }
  .brand-front__text { margin-left: 36px; color: var(--mark-grey); text-align: center; }
  .brand-name {
    display: block; font-weight: 500; letter-spacing: 0.02em; line-height: 1;
  }
  .brand-front .brand-name { font-size: 66px; }
  .brand-sub {
    display: flex; align-items: center; justify-content: center; gap: 10px;
    font-weight: 500; letter-spacing: 0.03em; line-height: 1; margin-top: 6px;
  }
  .brand-sub::before, .brand-sub::after {
    content: ""; display: block; height: 1.5px; background: currentColor; flex: 1;
  }
  .brand-front .brand-sub { font-size: 25px; }

  /* person */
  .person { position: absolute; left: 79px; top: 280px; color: var(--ink); }
  .person__name { font-size: 41px; font-weight: 400; line-height: 1; }
  .person__title { font-size: 19px; margin-top: 10px; letter-spacing: 0.01em; }

  /* contact */
  .contact {
    position: absolute; right: 62px; top: 322px;
    color: var(--ink); text-align: right; font-style: normal;
    font-size: 25px; line-height: 39px;
  }

  /* back logo */
  .brand-back {
    position: absolute; left: 0; right: 0; top: 118px;
    display: flex; flex-direction: column; align-items: center; color: var(--paper);
  }
  .brand-back__dot { width: 190px; height: 190px; border-radius: 50%; background: var(--paper); }
  .brand-back .brand-name { font-size: 50px; margin-top: 46px; }
  .brand-back .brand-sub { font-size: 20px; margin-top: 4px; width: 420px; }
</style>
</head>
<body>
<main class="canvas">
  <section class="card card--front" aria-label="Card front">
    <div class="brand-front">
      <div class="brand-front__dot"></div>
      <div class="brand-front__text">
        <span class="brand-name">TARNWELL</span>
        <span class="brand-sub">BUILDING CONSULTANTS</span>
      </div>
    </div>
    <div class="person">
      <h1 class="person__name">Dorwen Halket</h1>
      <p class="person__title">ADBldg Surv DIRECTOR</p>
    </div>
    <address class="contact">
      57 Quillon Rise,<br>
      Marrick Heights WA 6148<br>
      Mobile 0438 271 594<br>
      Dorwen.halket@tarnwellpq.com
    </address>
  </section>

  <section class="card card--back" aria-label="Card back">
    <div class="brand-back">
      <div class="brand-back__dot"></div>
      <span class="brand-name">TARNWELL</span>
      <span class="brand-sub">BUILDING CONSULTANTS</span>
    </div>
  </section>
</main>
</body>
</html>
```